copper kettle drywall repair web page

need a web presence for my company. we are a golf themed drywall repair company. need a home page, contact us, photos, about us, services possible payment option

```html
<!DOCTYPE html>
<html lang="en">
<head>
<meta charset="utf-8">
<title>Copper Kettle Drywall Repair</title>
<link rel="stylesheet" href="https://fonts.googleapis.com/css2?family=Fira+Sans:wght@400;600&display=swap">
<style>
  :root {
    --navy: #1f2a5e;
    --gold: #c9a22a;
    --white: #ffffff;
    --frame: #b8b8b8;
    --footer-band: rgba(60, 60, 60, 0.62);
    --link: #3d78b8;
    --ink: #2b2b2b;
  }
  * { box-sizing: border-box; margin: 0; padding: 0; }
  html, body {
    width: 1200px;
    height: 975px;
    overflow: hidden;
    background: var(--white);
    font-family: "Fira Sans", Arial, sans-serif;
  }
  .page {
    position: relative;
    width: 1200px;
    height: 975px;
  }
  .page-frame {
    position: absolute;
    inset: 14px 14px 12px 14px;
    border: 2px solid var(--frame);
    pointer-events: none;
  }
  .brand {
    position: absolute;
    top: 92px;
    left: 0;
    width: 1200px;
    display: flex;
    justify-content: center;
    align-items: center;
    gap: 14px;
  }
  .brand-dot {
    width: 34px;
    height: 34px;
    border-radius: 50%;
    background: var(--gold);
  }
  .brand-name {
    color: var(--navy);
    font-weight: 600;
    font-size: 34px;
    letter-spacing: 0.5px;
  }
  .tiles {
    position: absolute;
    top: 233px;
    left: 99px;
    display: grid;
    grid-template-columns: repeat(5, 190px);
    grid-template-rows: repeat(2, 306px);
    gap: 13px;
  }
  .tile {
    position: relative;
    color: var(--white);
    overflow: hidden;
  }
  .tile--navy { background: var(--navy); }
  .tile--gold { background: var(--gold); }
  .tile-icon {
    position: absolute;
    left: 0;
    width: 100%;
    display: flex;
    justify-content: center;
  }
  .tile-icon svg { display: block; }
  .tile-title {
    position: absolute;
    left: 19px;
    right: 12px;
    font-weight: 600;
    font-size: 25px;
    line-height: 23px;
  }
  .tile-text {
    position: absolute;
    left: 19px;
    right: 16px;
    font-size: 14.5px;
    line-height: 23px;
  }
  .more-tab {
    position: absolute;
    right: 0;
    bottom: 16px;
    width: 78px;
    height: 22px;
    background: var(--white);
    clip-path: polygon(14px 0, 100% 0, 100% 100%, 0 100%);
    color: var(--ink);
    font-size: 14px;
    line-height: 22px;
    text-align: center;
    padding-left: 10px;
  }
  .photo {
    width: 100%;
    height: 100%;
  }
  .photo--stucco { background: linear-gradient(90deg, #d6d6d6, #8f8f8f 30%, #e2e2e2 55%, #9a9a9a 80%, #cfcfcf); }
  .photo--brick-diagonal { background: linear-gradient(135deg, #b9b9b9 0%, #6e6e6e 40%, #3d3d3d 70%, #2a2a2a 100%); }
  .photo--brick-wall { background: linear-gradient(90deg, #5c5c5c 0%, #4a4a4a 70%, #2c2c2c 72%, #3a3a3a 100%); }
  .photo--ribbed { background: linear-gradient(90deg, #efefef, #777 25%, #f0f0f0 50%, #6f6f6f 75%, #e8e8e8); }
  .photo--tiles { background: linear-gradient(180deg, #a5a39f, #8c8b86 50%, #9fa3a0 100%); }
  .footer {
    position: absolute;
    left: 0;
    top: 810px;
    width: 1200px;
    height: 165px;
    background: var(--footer-band);
  }
  .footer-nav {
    position: absolute;
    left: 121px;
    top: 89px;
    font-size: 14.5px;
    color: var(--link);
  }
  .footer-nav a { color: var(--link); text-decoration: none; }
  .footer-nav .sep { margin: 0 4px; }
  .copyright {
    position: absolute;
    right: 110px;
    top: 89px;
    font-size: 14.5px;
    color: var(--ink);
  }
</style>
</head>
<body>
<div class="page">
  <div class="page-frame"></div>

  <header class="brand">
    <span class="brand-dot"></span>
    <span class="brand-name">Copper Kettle Drywall Repair</span>
  </header>

  <main class="tiles">
    <a class="tile tile--navy">
      <div class="tile-icon" style="top:30px">
        <svg width="78" height="78" viewBox="0 0 78 78" fill="#fff">
          <circle cx="39" cy="22" r="16"/>
          <path d="M8 76 C8 52 20 42 39 42 C58 42 70 52 70 76 Z"/>
          <path d="M36 44 L42 44 L44 66 L39 72 L34 66 Z" fill="#1f2a5e"/>
        </svg>
      </div>
      <h2 class="tile-title" style="top:122px">About Us</h2>
      <p class="tile-text" style="top:160px">Find out more about our business...</p>
      <span class="more-tab">More</span>
    </a>

    <div class="tile"><div class="photo photo--stucco" role="img" aria-label="Close-up photo of textured stucco wall"></div></div>

    <a class="tile tile--navy">
      <div class="tile-icon" style="top:30px">
        <svg width="82" height="82" viewBox="0 0 82 82" fill="none" stroke="#fff" stroke-linecap="round">
          <path d="M14 14 L66 66" stroke-width="9"/>
          <path d="M8 8 L20 4 L24 16 L16 22 Z" fill="#fff" stroke-width="2"/>
          <path d="M62 20 L22 62" stroke-width="7"/>
          <path d="M56 10 A13 13 0 1 0 72 26 L64 26 L56 18 Z" fill="#fff" stroke-width="2"/>
          <circle cx="16" cy="68" r="8" fill="#fff" stroke-width="2"/>
        </svg>
      </div>
      <h2 class="tile-title" style="top:122px">Services</h2>
      <p class="tile-text" style="top:160px">Check out the services we offer.</p>
      <span class="more-tab">More</span>
    </a>

    <div class="tile"><div class="photo photo--brick-diagonal" role="img" aria-label="Photo of a brick wall with diagonal shadow"></div></div>

    <a class="tile tile--navy">
      <div class="tile-icon" style="top:40px">
        <svg width="80" height="66" viewBox="0 0 80 66" fill="none" stroke="#fff" stroke-width="4" stroke-linejoin="round">
          <rect x="14" y="4" width="62" height="46" rx="4"/>
          <rect x="4" y="14" width="62" height="46" rx="4" fill="#1f2a5e"/>
          <circle cx="20" cy="28" r="5" fill="#fff" stroke="none"/>
          <path d="M10 54 L28 36 L38 46 L48 34 L60 54 Z" fill="#fff" stroke="none"/>
        </svg>
      </div>
      <h2 class="tile-title" style="top:122px">Gallery</h2>
      <p class="tile-text" style="top:160px">Take a look at our before &amp; after photos.</p>
      <span class="more-tab">More</span>
    </a>

    <div class="tile"><div class="photo photo--brick-wall" role="img" aria-label="Photo of a dark painted brick wall"></div></div>

    <a class="tile tile--gold">
      <div class="tile-icon" style="top:42px">
        <svg width="86" height="62" viewBox="0 0 86 62" fill="none" stroke="#fff" stroke-width="5">
          <rect x="4" y="4" width="78" height="54" rx="9"/>
          <line x1="4" y1="20" x2="82" y2="20"/>
          <line x1="14" y1="40" x2="40" y2="40"/>
          <circle cx="62" cy="41" r="6" fill="#fff"/>
          <circle cx="70" cy="41" r="6" fill="#fff"/>
        </svg>
      </div>
      <h2 class="tile-title" style="top:124px">Payment<br>Methods</h2>
      <p class="tile-text" style="top:182px">Choose any of our current payment options.</p>
      <span class="more-tab">More</span>
    </a>

    <div class="tile"><div class="photo photo--ribbed" role="img" aria-label="Photo of vertical ribbed wall panels"></div></div>

    <a class="tile tile--gold">
      <div class="tile-icon" style="top:44px">
        <svg width="76" height="58" viewBox="0 0 76 58" fill="#fff">
          <path d="M4 20 C4 6 72 6 72 20 L72 26 L56 26 L56 18 L20 18 L20 26 L4 26 Z"/>
          <path d="M18 26 L58 26 L70 54 L6 54 Z"/>
          <circle cx="38" cy="38" r="10" fill="#c9a22a"/>
          <circle cx="38" cy="38" r="4"/>
        </svg>
      </div>
      <h2 class="tile-title" style="top:122px">Contact Us</h2>
      <p class="tile-text" style="top:160px">Have a question or need help?</p>
      <span class="more-tab">More</span>
    </a>

    <div class="tile"><div class="photo photo--tiles" role="img" aria-label="Photo of grey stone tile wall"></div></div>
  </main>

  <footer class="footer">
    <nav class="footer-nav">
      <a>About Us</a><span class="sep">|</span><a>Services</a><span class="sep">|</span><a>Gallery</a><span class="sep">|</span><a>Payment Methods</a><span class="sep">|</span><a>Contact Us</a>
    </nav>
    <p class="copyright">Copyright © 2015 Copper Kettle</p>
  </footer>
</div>
</body>
</html>
```